**URGENT // ENVIRONMENTAL // QUICK TURN AROUND**

We are looking for an A-Grade designer to work with longterm, starting with the successful design for our website & logo; Pelham Grove.

Pelham Grove is a business that focusses on grouping environmentally conscious people together and helping them get "bulk buy" discounts by purchasing large volumes together; solar, energy efficency, wind turbines, and the like.

The Logo and website must have a green feel, as we are here to protect the environment, whilst also helping our customers save money.

The website must also have a blog feature, allowing us to post and keep people up to date with the latest in the industry.

Target Market(s)

FAMILIES WITHIN REGIONAL AUSTRALIA WANTING TO EITHER SAVE MONEY ON ELECTRICITY BILLS, OR REDUCE CARBON EMISSIONS.

Industry/Entity Type

Solar Energy

Logo Text

PELHAM GROVE

Number of Pages Required

5+ page

Font styles to use
Serif
Sans Serif

Colors

Designer to choose colors to be used in the design.

Requirements
Must have
• 1.HOME PAGE
• 2.OUR SERVICES PAGE
• - RENEWABLE ENERGY
• - LIGHTING SYSTEMS
• - ENERGY ASSESSMENT
• - R.G.L.C SCHEME
• - ENERGY COMPARISON
• 4. BOOK AN APPOINTMENT
• 5. IN THE NEWS
• 6. SUBSCRIBE TO NEWSLETTER
• 7. CONTACT US
• MUST LOOK VERY PROFESSIONAL, WITH LOTS OF INFORMATION, IT CANNOT BE BARE AND SIMPLE.
• Can use www.marlowfieldtrading.com.au which is our other brand for copy and ideas - HOWEVER, THIS IS THE REASON WE ARE RE-BRANDING, AS THIS BRAND HAS COME UNDER FAR TOO MUCH CRITICISM FOR LACK OF INFORMATION AND LOOKING TO SIMPLE.
Nice to have
• BLOG FEATURE
Should not have
• ANYTHING THAT APPEARS NON-ENVIRONMENTALS

```html
<!DOCTYPE html>
<html lang="en">
<head>
<meta charset="utf-8">
<title>Pelham Grove — Home</title>
<link rel="stylesheet" href="https://fonts.googleapis.com/css2?family=Lora:wght@400;500&family=Merriweather:wght@300;400&family=Lato:wght@400;700&display=swap">
<style>
  :root {
    --backdrop: #ececec;
    --page: #ffffff;
    --green: #4caf2a;
    --green-light: #8cc63f;
    --green-panel: #5aa936;
    --green-dark: #1f6b2a;
    --ink: #333a3a;
    --muted: #6b7272;
    --hero-deep: #1d3550;
    --hero-mid: #3d5f80;
    --white: #ffffff;
  }
  * { box-sizing: border-box; margin: 0; padding: 0; }
  html, body { width: 1000px; height: 1200px; overflow: hidden; }
  body { background: var(--backdrop); font-family: "Lato", sans-serif; position: relative; }

  .page { position: absolute; left: 105px; top: 0; width: 815px; height: 1195px; background: var(--page); box-shadow: 0 0 18px rgba(0,0,0,.18); }

  /* Hero */
  .hero { position: absolute; left: 0; top: 0; width: 815px; height: 369px;
    background: radial-gradient(circle at 380px 70px, #8a9aa8 0, #51708d 90px, transparent 220px),
                linear-gradient(120deg, var(--hero-deep) 0%, #2b4868 45%, var(--hero-mid) 75%, #6f8aa5 100%); }
  .hero-shade { position: absolute; inset: 0; background: rgba(20,35,55,.25); }
  .brand { position: absolute; left: 118px; top: 21px; display: flex; align-items: center; gap: 8px;
    font-family: "Lora", serif; font-size: 18px; color: var(--white); }
  .brand-dot { width: 12px; height: 12px; border-radius: 50%; background: var(--white); }
  .nav { position: absolute; left: 314px; top: 22px; display: flex; gap: 0; list-style: none;
    font-family: "Lora", serif; font-size: 8.5px; letter-spacing: .2px; color: var(--white); }
  .nav li { padding: 0 8px 7px; }
  .nav .is-active { color: var(--green-light); border-bottom: 2px solid var(--green); }
  .search { position: absolute; left: 615px; top: 21px; width: 45px; height: 12px; background: var(--white); border-radius: 1px; }
  .search svg { position: absolute; right: 3px; top: 2px; }
  .mission { position: absolute; top: 131px; left: 0; width: 815px; text-align: center;
    font-family: "Lora", serif; font-size: 16px; letter-spacing: .4px; color: var(--white); }
  .hero-title { position: absolute; top: 182px; left: 0; width: 815px; text-align: center;
    font-family: "Lora", serif; font-weight: 400; font-size: 25.5px; line-height: 31px; color: var(--white); }
  .slider-dots { position: absolute; left: 370px; top: 267px; display: flex; align-items: center; gap: 5px; }
  .slider-dots .bar { width: 35px; height: 1px; background: rgba(255,255,255,.6); }
  .slider-dots .dot { width: 4px; height: 4px; border-radius: 50%; background: var(--green-light); }
  .btn-subscribe { position: absolute; left: 301px; top: 291px; width: 218px; height: 25px; background: var(--green);
    color: var(--white); font-family: "Lora", serif; font-size: 15.5px; line-height: 25px; text-align: center; border-radius: 1px; }
  .arrow { position: absolute; top: 187px; width: 19px; height: 19px; display: flex; align-items: center; justify-content: center; }
  .arrow-prev { left: 21px; background: rgba(255,255,255,.25); }
  .arrow-next { left: 780px; background: var(--green); }

  /* Features */
  .features { position: absolute; top: 369px; left: 0; width: 815px; height: 286px; }
  .feature { position: absolute; top: 0; width: 230px; text-align: center; }
  .feature svg { display: block; margin: 52px auto 0; }
  .feature h3 { margin-top: 17px; font-family: "Merriweather", serif; font-weight: 300; font-size: 14px; color: var(--ink); }
  .feature p { margin-top: 11px; font-size: 9px; line-height: 13.5px; color: var(--muted); }

  /* Environment block */
  .forest { position: absolute; left: 0; top: 655px; width: 497px; height: 527px;
    background: radial-gradient(circle at 200px 250px, #6f9a3a 0, transparent 230px),
                linear-gradient(160deg, #9fbf6a 0%, #4f7a2c 40%, #2d4a1d 75%, #a9a08a 100%); }
  .protect { position: absolute; left: 497px; top: 655px; width: 318px; height: 527px;
    background: radial-gradient(circle at 230px 80px, #86c24a 0, transparent 160px),
                linear-gradient(180deg, #66b23c 0%, var(--green-panel) 50%, #4f9f2e 100%); color: var(--white); padding-left: 32px; }
  .protect h2 { margin-top: 48px; font-family: "Merriweather", serif; font-weight: 400; font-size: 28px; line-height: 29px; }
  .protect .rule { width: 73px; height: 1px; background: var(--white); margin-top: 18px; }
  .protect .lead { margin-top: 17px; font-size: 10.5px; font-weight: 700; }
  .steps { list-style: none; margin-top: 20px; }
  .steps li { display: flex; height: 75px; }
  .steps .num { width: 43px; font-family: "Merriweather", serif; font-weight: 300; font-size: 22px; line-height: 24px; }
  .steps p { width: 222px; font-size: 9.5px; line-height: 17.7px; padding-top: 2px; }
  .btn-more { display: inline-block; margin-top: 4px; width: 126px; height: 29px; line-height: 29px; text-align: center;
    background: var(--green-dark); font-size: 10px; font-weight: 700; color: var(--white); }
</style>
</head>
<body>
<div class="page">
  <header class="hero" role="img" aria-label="Photo of solar panels under a sunny blue sky">
    <div class="hero-shade"></div>
  </header>
  <div class="brand"><span class="brand-dot"></span>Pelham Grove</div>
  <ul class="nav">
    <li class="is-active">HOME</li><li>ABOUT US</li><li>RECENT NEWS</li><li>PROGRAM</li><li>CONTACT</li>
  </ul>
  <div class="search"><svg width="7" height="7" viewBox="0 0 7 7"><circle cx="3" cy="3" r="2" fill="none" stroke="#333" stroke-width="1"/><line x1="4.5" y1="4.5" x2="6.5" y2="6.5" stroke="#333" stroke-width="1"/></svg></div>
  <p class="mission">Our mission is to provide affordable green energy for all.</p>
  <h1 class="hero-title">Learn how our solar solutions<br>affect the environment and society as a whole.</h1>
  <div class="slider-dots"><span class="bar"></span><span class="dot"></span><span class="bar"></span></div>
  <div class="btn-subscribe">Subscribe Our Newsletter</div>
  <div class="arrow arrow-prev"><svg width="8" height="8" viewBox="0 0 8 8"><path d="M5.5 1 L2.5 4 L5.5 7" fill="none" stroke="#fff" stroke-width="1.2"/></svg></div>
  <div class="arrow arrow-next"><svg width="8" height="8" viewBox="0 0 8 8"><path d="M2.5 1 L5.5 4 L2.5 7" fill="none" stroke="#fff" stroke-width="1.2"/></svg></div>

  <section class="features">
    <svg width="0" height="0"><defs><linearGradient id="iconGrad" x1="0" y1="0" x2="0" y2="1"><stop offset="0" stop-color="#9ccd3c"/><stop offset="1" stop-color="#3fa43a"/></linearGradient></defs></svg>
    <div class="feature" style="left:47px">
      <svg width="104" height="104" viewBox="0 0 104 104" fill="none" stroke="url(#iconGrad)" stroke-width="2.5">
        <circle cx="52" cy="24" r="19"/><circle cx="28" cy="50" r="19"/><circle cx="76" cy="50" r="19"/>
        <path d="M52 58 Q52 85 64 103"/>
      </svg>
      <h3>Vivamus blandit</h3>
      <p>Sed ut interdum lectus, eu ultrices mauris. Aenean eu<br>massa lobortis commodo</p>
    </div>
    <div class="feature" style="left:297px">
      <svg width="104" height="100" viewBox="0 0 104 100" fill="none" stroke="url(#iconGrad)" stroke-width="2.5">
        <path d="M48 62 C30 50 20 30 25 2 C50 10 58 35 48 62 Z"/><path d="M52 64 C58 45 72 38 92 36 C88 55 72 64 52 64 Z"/>
        <rect x="2" y="66" width="14" height="28"/><path d="M16 70 H60 Q66 74 60 78 H40 M16 92 H60 L100 76"/>
      </svg>
      <h3>Proin enim cras</h3>
      <p>Aliquam eleifend magna a mauris lacinia, ut aliquet elit<br>feugiat. Donec a dapibus dolor</p>
    </div>
    <div class="feature" style="left:547px">
      <svg width="80" height="104" viewBox="0 0 80 104" fill="none" stroke="url(#iconGrad)" stroke-width="2.5">
        <path d="M26 74 C10 64 2 52 2 40 A38 38 0 0 1 78 40 C78 52 70 64 54 74 Z"/>
        <path d="M40 70 V20 M40 20 C26 34 26 52 40 58 C54 52 54 34 40 20"/>
        <line x1="28" y1="82" x2="52" y2="82"/><line x1="28" y1="90" x2="52" y2="90"/><line x1="32" y1="98" x2="48" y2="98"/>
      </svg>
      <h3>Etiam venenatis</h3>
      <p>Curabitur ultrices dui sit amet varius tincidunt. Nullam<br>ullamcorper ipsum condimentum</p>
    </div>
  </section>

  <div class="forest" role="img" aria-label="Photo of a wooden boardwalk winding through a lush fern forest"></div>
  <section class="protect">
    <h2>Ways of<br>protecting<br>the environment</h2>
    <div class="rule"></div>
    <p class="lead">Donec blandit luctus laoreet. Donec dui arcu dapibus</p>
    <ol class="steps">
      <li><span class="num">1.</span><p>Etiam finibus auctor sagittis. Phasellus ac tempor odio. Donec scelerisque ullamcorper felis, id sagittis dolor.</p></li>
      <li><span class="num">2.</span><p>Nunc tempus porttitor ipsum, quis cursus nisl fringilla non. Cras id eros molestie, iaculis dolor eu, vulputate tellus velit.</p></li>
      <li><span class="num">3.</span><p>Proin id molestie lorem, sed venenatis orci. Curabitur a lorem sed sem bibendum porttitor varius sit amet sem.</p></li>
    </ol>
    <span class="btn-more">Read more about us</span>
  </section>
</div>
</body>
</html>
```